Responsive, beautiful email sign-up process pages

My client wants to re-imagine their email newsletter sign up process. The funnel currently starts in the first panel of their home page carousel at:

https://thriftbeacon.co.uk/

It is also featured in the right side of the footer.

I would like to start, what could become a full template re-design project by optimising this crucial user journey. I am attaching the screenshots from the current user journey below and it would be great to get some designs that improve on the look and feel.

Thank you,
Gideon

Target Market(s)

People who want to maximise the interest rate they receive on their cash savings.

Industry/Entity Type

Financial Service

Coding

Coded - Design and coding required

Number of Pages Required

4 page

Font styles to use
Sans Serif

Requirements
Must have
• A well designed, responsive design for all of the elements of the user journey funnel that works well on desktop, laptop, tablet and phone. The site is currently using Bootstrap 3.* for the responsive templates, so it would be useful to continue leveraging these libraries, but in a much more visually appealing way.
• It is felt that the current overall site is dull and unprofessional, so we are using this as a way of showing how much better it could be, which should lead to a sitewide "facelift".
Nice to have
• Creative use of css, svg and javascript to optimise the user experience on all target platforms.
Should not have
• Non-responsive designs.

```html
<!DOCTYPE html>
<html lang="en">
<head>
<meta charset="utf-8">
<title>Thrift Beacon – Better deals for savers</title>
<link href="https://fonts.googleapis.com/css2?family=Open+Sans:wght@300;400;600;700&display=swap" rel="stylesheet">
<style>
:root{
  --orange:#f28a1c;
  --orange-dark:#d9740c;
  --ink:#2e2e2e;
  --text:#555;
  --muted:#8a8a8a;
  --line:#e2e2e2;
  --band:#f2f2f2;
  --panel:#e6e6e6;
  --dark:#333;
  --darker:#262626;
  --white:#fff;
}
*{box-sizing:border-box;margin:0;padding:0}
html,body{width:1200px;height:3840px;overflow:hidden}
body{font-family:"Open Sans",Arial,sans-serif;color:var(--text);background:var(--white);font-size:13px;line-height:1.5}
.wrap{width:1040px;margin:0 auto;position:relative}
a{color:inherit;text-decoration:none}
.orange-link{color:var(--orange);font-size:10px;font-weight:700;letter-spacing:.5px;text-transform:uppercase}

/* header */
.site-header{height:52px;border-bottom:1px solid var(--line)}
.site-header .wrap{display:flex;align-items:center;height:52px}
.brand{display:flex;align-items:center;gap:8px;font-weight:700;font-size:17px;color:var(--ink);width:300px}
.brand-dot{width:22px;height:22px;border-radius:50%;background:var(--orange)}
.main-nav{display:flex;gap:34px;font-size:10px;font-weight:600;letter-spacing:1px;color:var(--text);flex:1;justify-content:center;padding-right:80px}
.account{display:flex;gap:18px;font-size:11px;font-weight:600;color:var(--ink)}

.subnav{background:var(--orange);height:36px;color:var(--white);font-size:11px;font-weight:600}
.subnav .wrap{display:flex;align-items:center;height:36px;gap:34px}
.search{margin-left:auto;width:250px;height:24px;background:var(--white);border-radius:2px;color:var(--muted);font-weight:400;font-size:11px;padding:4px 10px}

/* hero */
.hero{height:512px;background:linear-gradient(90deg,#3a332d 0%,#5b5047 45%,#8a7c70 70%,#6a5e55 100%);position:relative;color:var(--white)}
.hero-photo{position:absolute;inset:0}
.hero .wrap{padding-top:110px}
.hero h1{font-size:46px;font-weight:700;line-height:1.1;letter-spacing:-.5px}
.hero .lead{font-size:17px;font-weight:600;margin:12px 0 14px}
.hero ul{list-style:none;font-size:12px;font-weight:600;line-height:1.9}
.hero li::before{content:"";display:inline-block;width:6px;height:6px;border-radius:50%;background:var(--orange);margin-right:8px;vertical-align:middle}
.signup{display:flex;margin-top:30px;gap:10px}
.signup .field{width:210px;height:36px;border:1px solid rgba(255,255,255,.7);border-radius:18px;font-size:11px;padding:9px 16px;color:rgba(255,255,255,.85)}
.btn{display:inline-block;background:var(--orange);color:var(--white);font-size:10px;font-weight:700;letter-spacing:1px;text-transform:uppercase;height:36px;line-height:36px;padding:0 24px;border-radius:18px}

/* features */
.features{height:160px}
.features .wrap{display:flex;gap:40px;padding:34px 0 0 220px}
.feature{display:flex;gap:14px;width:250px}
.feature svg{flex:none}
.feature h3{font-size:12px;font-weight:600;color:var(--ink);margin-bottom:4px}
.feature p{font-size:10px;line-height:1.6;color:var(--muted)}

/* manage band */
.manage{background:var(--band);height:560px}
.manage .wrap{display:flex;justify-content:space-between;padding-top:60px}
.manage-copy{width:440px}
.manage h2{font-size:30px;font-weight:600;color:var(--ink);line-height:1.2;margin-bottom:14px}
.manage p{font-size:11px;color:var(--muted);line-height:1.7}
.manage h4{font-size:13px;font-weight:600;color:var(--ink);margin:26px 0 6px}
.manage .orange-link{display:block;margin-top:12px}
.callback{width:480px;background:var(--panel);padding:24px}
.callback h2{font-size:24px;margin-bottom:8px}
.callback .intro{font-size:10px;margin-bottom:8px}
.label{font-size:11px;color:var(--text);margin:12px 0 4px}
.input{height:30px;background:var(--white)}
.submit{margin-top:16px;height:34px;background:#5a5a5a;color:var(--white);text-align:center;font-size:11px;font-weight:700;letter-spacing:1.5px;line-height:34px}
.donate{margin-top:14px;background:#4a4a4a;color:var(--white);padding:16px 18px}
.donate strong{display:block;font-size:15px;font-weight:700}
.donate span{font-size:13px}
.donate .orange-link{color:var(--white);display:block;margin-top:10px}

/* how */
.how{height:560px;text-align:center}
.how h2{font-size:30px;font-weight:600;color:var(--ink);padding-top:74px}
.how .sub{font-size:11px;color:var(--muted);margin-top:8px}
.how .orange-link{display:block;margin-top:6px}
.steps{position:relative;display:flex;justify-content:space-between;width:860px;margin:56px auto 0}
.steps-line{position:absolute;left:120px;right:120px;top:34px;border-top:1px dashed #ccc}
.step{width:240px;position:relative}
.step-icon{width:68px;height:68px;border-radius:50%;background:var(--white);border:1px solid var(--line);margin:0 auto 34px;display:flex;align-items:center;justify-content:center}
.step h3{font-size:13px;font-weight:600;color:var(--ink);margin-bottom:6px}
.step p{font-size:10px;color:var(--muted);line-height:1.6}

/* access */
.access{height:440px;text-align:center;border-top:1px solid var(--line)}
.access h2{font-size:36px;font-weight:600;color:var(--ink);line-height:1.25;padding-top:130px}
.access .sub{font-size:9px;letter-spacing:1px;color:var(--muted);margin-top:22px}
.access .signup{justify-content:center;margin-top:8px}
.access .field{width:300px;border-color:#ccc;color:var(--muted)}

/* quote */
.quote{height:200px;text-align:center;border-top:1px solid var(--line)}
.quote blockquote{font-size:26px;font-weight:600;color:var(--ink);line-height:1.3;padding-top:56px}
.quote cite{display:block;font-style:normal;font-size:9px;letter-spacing:1px;color:var(--muted);margin-top:10px}

/* press */
.press{height:260px}
.press-grid{display:grid;grid-template-columns:repeat(6,1fr);width:860px;margin:20px auto 0;border-top:1px solid var(--line);border-left:1px solid var(--line)}
.badge{height:96px;border-right:1px solid var(--line);border-bottom:1px solid var(--line);display:flex;align-items:center;justify-content:center}
.badge i{display:block;width:90px;height:18px;background:#bdbdbd;border-radius:2px}
.badge i.round{width:44px;height:44px;border-radius:50%}

/* contact band */
.contact-band{background:var(--band);height:180px}
.contact-band .wrap{display:flex;align-items:center;height:180px}
.contact-band h3{font-size:15px;font-weight:700;color:var(--ink)}
.phone{font-size:26px;font-weight:700;color:var(--ink)}
.phone small{font-size:14px;font-weight:400}
.band-links{margin-left:auto;display:flex;gap:60px;font-size:11px;font-weight:700;letter-spacing:1px;color:var(--ink)}
.band-links span{display:flex;align-items:center;gap:12px}

/* offices */
.offices{height:500px}
.offices .wrap{display:flex;gap:70px;padding-top:40px}
.touch{width:380px}
.touch h2{font-size:34px;font-weight:600;color:var(--ink);margin-bottom:14px}
.touch p{font-size:11px;margin-bottom:10px;line-height:1.6}
.touch strong{color:var(--ink)}
.touch h4{font-size:18px;color:var(--ink);margin-top:16px}
.office-list{flex:1}
.office{display:flex;border-top:1px solid var(--line);padding:14px 0}
.office:last-child{border-bottom:1px solid var(--line)}
.office h5{font-size:11px;font-weight:700;letter-spacing:1px;color:var(--ink);margin-bottom:6px}
.office .addr{width:300px;font-size:11px;line-height:1.6}
.office .acts{display:flex;gap:40px;align-items:flex-end}

/* footer */
.site-footer{background:var(--dark);height:180px;color:#cfcfcf}
.site-footer .wrap{display:flex;gap:60px;padding-top:30px;font-size:9px;line-height:1.9;letter-spacing:.5px;text-transform:uppercase}
.site-footer ul{list-style:none;width:180px}
.footer-bottom{background:var(--darker);height:60px;color:#cfcfcf}
.footer-bottom .wrap{display:flex;align-items:center;height:60px;gap:20px;font-size:9px;letter-spacing:.5px}
.footer-bottom .social{margin-left:auto;display:flex;gap:10px}
.footer-bottom .social i{width:10px;height:10px;background:#aaa;display:block}
</style>
</head>
<body>

<header class="site-header">
  <div class="wrap">
    <a class="brand" href="#"><span class="brand-dot"></span>Thrift Beacon</a>
    <nav class="main-nav"><a>ABOUT</a><a>NEWS</a><a>AWARDS</a><a>CONTACT</a></nav>
    <div class="account"><a>Sign in</a><a>Register</a></div>
  </div>
</header>

<nav class="subnav">
  <div class="wrap">
    <span>All Sections ▾</span><span>Request a call back</span><span>Make an appointment</span>
    <div class="search">What are you looking for?</div>
  </div>
</nav>

<section class="hero">
  <div class="hero-photo" role="img" aria-label="Photo of an adviser meeting a smiling client across a desk in a bright office"></div>
  <div class="wrap">
    <h1>Better deals for savers.</h1>
    <p class="lead">Get free whole of market information.</p>
    <ul>
      <li>Comprehensive Best Buy Tables</li>
      <li>Account Monitoring and Alerts</li>
      <li>Access to Savings Experts</li>
    </ul>
    <div class="signup"><div class="field">Enter your e-mail address</div><a class="btn">Get advice</a></div>
  </div>
</section>

<section class="features">
  <div class="wrap">
    <div class="feature">
      <svg width="34" height="34" viewBox="0 0 34 34" fill="none" stroke="#f28a1c" stroke-width="1.5"><circle cx="12" cy="11" r="5"/><circle cx="23" cy="13" r="4"/><path d="M3 28c1-6 5-9 9-9s8 3 9 9M20 27c1-4 3-7 7-7 3 0 5 2 5 6"/></svg>
      <div><h3>Team of experts</h3><p>Over 20 years of experience with savings accounts and 50,000 savers who trust our independent tables and our clear guidance.</p></div>
    </div>
    <div class="feature">
      <svg width="34" height="34" viewBox="0 0 34 34" fill="none" stroke="#f28a1c" stroke-width="1.5"><path d="M17 3l11 4v9c0 8-5 13-11 15C11 29 6 24 6 16V7z"/><path d="M12 17l4 4 7-8"/></svg>
      <div><h3>Easy and safe</h3><p>Compare the top accounts in one place, with rates checked daily and every bank covered by the deposit guarantee scheme.</p></div>
    </div>
    <div class="feature">
      <svg width="34" height="34" viewBox="0 0 34 34" fill="none" stroke="#f28a1c" stroke-width="1.5"><circle cx="17" cy="17" r="13"/><path d="M21 11c-1-2-7-2-7 2 0 4 7 3 7 7 0 4-6 4-8 1M17 8v18"/></svg>
      <div><h3>You pay for what you get</h3><p>Our service is free to use, and when you choose a paid option you always see the price before you commit.</p></div>
    </div>
  </div>
</section>

<section class="manage">
  <div class="wrap">
    <div class="manage-copy">
      <h2>Manage your savings<br>effortlessly.</h2>
      <p>We know that keeping track of rates across many accounts takes time. Our tools watch your balances and rates for you, flag when a better deal appears and keep every account in one simple view.</p>
      <a class="orange-link">Learn more about our services ›</a>
      <h4>Rate tracking made easy</h4>
      <p>Add your accounts once and we will alert you the moment a rate drops or a bonus period ends.</p>
      <h4>Stay informed</h4>
      <p>Receive our newsletter with the latest best buys, market news and rate changes so you never miss an offer that suits your savings goals.</p>
      <h4>Better overall returns</h4>
      <p>Savers who move money when alerted earn more each year than those who leave it in old accounts.</p>
      <a class="orange-link">Learn more about managing your savings ›</a>
    </div>
    <div class="callback">
      <h2>Request a call-back.</h2>
      <p class="intro">Leave your details and one of our savings experts will call you back at a time that suits you, with no obligation.</p>
      <div class="label">Name</div><div class="input"></div>
      <div class="label">Phone number</div><div class="input"></div>
      <div class="label">Email address</div><div class="input"></div>
      <div class="submit">SUBMIT YOUR REQUEST</div>
      <div class="donate">
        <strong>Do you have over £100,000 on deposit?</strong>
        <span>We'll donate £50 to a charity of your choice.</span>
        <a class="orange-link">Learn more about our charity offer ›</a>
      </div>
    </div>
  </div>
</section>

<section class="how">
  <h2>How does it really work?</h2>
  <p class="sub">It's just a few simple steps – our experts can help you get the best overall return and keep your savings safe.</p>
  <a class="orange-link">Learn more about our services ›</a>
  <div class="steps">
    <div class="steps-line"></div>
    <div class="step">
      <div class="step-icon"><svg width="28" height="28" viewBox="0 0 28 28" fill="none" stroke="#f28a1c" stroke-width="1.5"><rect x="5" y="3" width="18" height="22" rx="2"/><path d="M9 9h10M9 14h10M9 19h6"/></svg></div>
      <h3>Select your savings account</h3>
      <p>Browse our independent tables and choose the account that fits your balance, access needs and term.</p>
    </div>
    <div class="step">
      <div class="step-icon"><svg width="28" height="28" viewBox="0 0 28 28" fill="none" stroke="#f28a1c" stroke-width="1.5"><path d="M4 20l6-6 5 4 9-10"/><path d="M18 8h6v6"/></svg></div>
      <h3>Receive good deals</h3>
      <p>Get alerts and regular updates whenever a better rate becomes available for your money.</p>
    </div>
    <div class="step">
      <div class="step-icon"><svg width="28" height="28" viewBox="0 0 28 28" fill="none" stroke="#f28a1c" stroke-width="1.5"><path d="M5 10h17l-4-4M23 18H6l4 4"/></svg></div>
      <h3>Switch for better deals</h3>
      <p>Move your savings in a few clicks and keep earning the best return on every pound.</p>
    </div>
  </div>
</section>

<section class="access">
  <h2>It's time to get access to<br>your free services.</h2>
  <p class="sub">JUST ENTER YOUR EMAIL ADDRESS</p>
  <div class="signup"><div class="field">Enter your e-mail address</div><a class="btn">Get advice</a></div>
</section>

<section class="quote">
  <blockquote>“Thrift Beacon is a great website for the beleaguered<br>saver. Unbiased and informative.”</blockquote>
  <cite>MONEY WEEKLY REVIEW, PERSONAL FINANCE EDITOR</cite>
</section>

<section class="press" aria-label="As featured in the press">
  <div class="press-grid">
    <div class="badge"><i></i></div><div class="badge"><i></i></div><div class="badge"><i class="round"></i></div>
    <div class="badge"><i></i></div><div class="badge"><i></i></div><div class="badge"><i></i></div>
    <div class="badge"><i class="round"></i></div><div class="badge"><i class="round"></i></div><div class="badge"><i></i></div>
    <div class="badge"><i></i></div><div class="badge"><i></i></div><div class="badge"><i></i></div>
  </div>
</section>

<section class="contact-band">
  <div class="wrap">
    <div>
      <h3>Speak Direct to a Savings Expert</h3>
      <div class="phone"><small>Call us </small>0800 555 0142</div>
    </div>
    <div class="band-links">
      <span><svg width="26" height="26" viewBox="0 0 26 26" fill="none" stroke="#2e2e2e" stroke-width="1.5"><path d="M7 3l4 5-2 3c1 3 3 5 6 6l3-2 5 4-2 4C12 23 3 14 3 5z"/></svg>REQUEST A CALL BACK</span>
      <span><svg width="26" height="26" viewBox="0 0 26 26" fill="none" stroke="#2e2e2e" stroke-width="1.5"><rect x="3" y="6" width="20" height="14"/><path d="M3 6l10 8 10-8"/></svg>WRITE US AN E-MAIL</span>
    </div>
  </div>
</section>

<section class="offices">
  <div class="wrap">
    <div class="touch">
      <h2>Get in touch.</h2>
      <p>Due to some of the specialist cases that we handle it is sometimes necessary for us to meet clients in our satellite offices in London and Leeds.</p>
      <p><strong>Please note that appointments held at these offices are strictly by appointment only.</strong></p>
      <p>Bath is our Head Office and clients are welcome to visit us by prior appointment.</p>
      <p>The Bath office is where the following functions of Thrift Beacon are based: Savings Advisers, Research Team, Media Team and IT.</p>
      <h4>Office hours</h4>
      <p>Monday – Friday: 9:00am – 5:30pm<br>Saturday: 10:00am – 1:00pm</p>
    </div>
    <div class="office-list">
      <div class="office">
        <div class="addr"><h5>BATH — HEAD OFFICE</h5>Beacon House, Lower Mill Street<br>Bath, BA1 9XX</div>
        <div class="acts"><a class="orange-link">◎ Make an appointment</a><a class="orange-link">◎ See on map</a></div>
      </div>
      <div class="office">
        <div class="addr"><h5>LONDON — SATELLITE OFFICE</h5>Central Court, 14 Fenwick Buildings<br>London, EC2A 9XX</div>
        <div class="acts"><a class="orange-link">◎ See on map</a></div>
      </div>
      <div class="office">
        <div class="addr"><h5>LEEDS — SATELLITE OFFICE</h5>Unit 7, The Arcade<br>Leeds, LS1 9XX</div>
        <div class="acts"><a class="orange-link">◎ See on map</a></div>
      </div>
    </div>
  </div>
</section>

<footer>
  <div class="site-footer">
    <div class="wrap">
      <ul><li>About us</li><li>Rate tracker</li><li>Advice and guides</li><li>Awards</li><li>Testimonials</li><li>Contact us</li></ul>
      <ul><li>Best buy overview</li><li>Fixed rate bonds</li><li>Easy access accounts</li><li>Notice accounts</li><li>Cash ISAs</li><li>Business savings</li></ul>
      <ul><li>Partner accounts</li><li>Savings calculator</li><li>Charity offer</li><li>Newsletter</li><li>Press centre</li><li>Careers</li></ul>
    </div>
  </div>
  <div class="footer-bottom">
    <div class="wrap">
      <span>ABOUT US</span><span>PRESS</span><span>NEWS</span>
      <span style="margin-left:40px">© THRIFT BEACON LTD</span><span>PRIVACY POLICY · TERMS</span>
      <div class="social"><i></i><i></i><i></i></div>
    </div>
  </div>
</footer>

</body>
</html>
```